Everything fresh, everything new

When I take over the practice, I would like to breathe new life into the practice. I want a business card design that catches the eye and brings a breath of fresh air

```html
<!DOCTYPE html>
<html lang="de">
<head>
<meta charset="utf-8">
<title>Praxis Frischwind – Visitenkarte</title>
<link rel="stylesheet" href="https://fonts.googleapis.com/css2?family=Montserrat:wght@600;700&family=Open+Sans:wght@400;600&display=swap">
<style>
  :root {
    --bg: #4a4a4a;
    --green: #8dc63f;
    --ink: #3d3d3f;
    --white: #ffffff;
  }
  * { box-sizing: border-box; margin: 0; padding: 0; }
  html, body { width: 1200px; height: 780px; overflow: hidden; }
  body {
    background: var(--bg);
    position: relative;
    font-family: "Open Sans", Arial, sans-serif;
    color: var(--ink);
  }
  .card {
    position: absolute;
    top: 232px;
    width: 550px;
    height: 315px;
    border-radius: 26px;
    box-shadow: 0 14px 30px rgba(0,0,0,.35);
    overflow: hidden;
  }
  .card--front { left: 40px; background: var(--white); border-bottom: 8px solid var(--green); }
  .card--back { left: 610px; background: var(--green); }

  .brand {
    position: absolute;
    display: flex;
    align-items: center;
    font-family: "Montserrat", Arial, sans-serif;
    font-weight: 700;
    white-space: nowrap;
  }
  .brand__dot {
    flex: none;
    border-radius: 50%;
    border-style: solid;
  }
  .card--front .brand { left: 32px; top: 140px; font-size: 20px; color: var(--ink); gap: 8px; }
  .card--front .brand__dot { width: 22px; height: 22px; border-width: 4px; border-color: var(--green); }
  .card--back .brand { left: 50%; top: 50%; transform: translate(-50%, -50%); font-size: 40px; color: var(--white); gap: 14px; }
  .card--back .brand__dot { width: 40px; height: 40px; border-width: 6px; border-color: var(--white); }

  .divider {
    position: absolute;
    left: 292px; top: 62px;
    width: 2px; height: 190px;
    background: var(--green);
  }
  .contact { position: absolute; left: 314px; top: 60px; }
  .contact__name {
    font-family: "Montserrat", Arial, sans-serif;
    font-weight: 700;
    font-size: 21px;
    line-height: 1.1;
    color: var(--ink);
  }
  .contact__name .first { color: var(--green); }
  .contact__role { font-size: 12px; margin-bottom: 18px; }
  .contact__list { list-style: none; font-size: 12px; line-height: 1.7; }
  .contact__list li { display: flex; align-items: center; gap: 8px; }
  .contact__list svg { width: 12px; height: 12px; fill: var(--green); flex: none; }
  .contact__address { margin-top: 16px; font-size: 12px; line-height: 1.5; }
</style>
</head>
<body>
  <section class="card card--front" aria-label="Vorderseite">
    <div class="brand"><span class="brand__dot"></span>Praxis Frischwind</div>
    <div class="divider"></div>
    <div class="contact">
      <p class="contact__name"><span class="first">Jonas</span> Weber</p>
      <p class="contact__role">Managing Director</p>
      <ul class="contact__list">
        <li><svg viewBox="0 0 24 24" aria-hidden="true"><path d="M6.6 10.8a15.1 15.1 0 0 0 6.6 6.6l2.2-2.2a1 1 0 0 1 1-.25 11.4 11.4 0 0 0 3.6.57 1 1 0 0 1 1 1V20a1 1 0 0 1-1 1A17 17 0 0 1 3 4a1 1 0 0 1 1-1h3.5a1 1 0 0 1 1 1c0 1.25.2 2.45.57 3.57a1 1 0 0 1-.25 1z"/></svg>030 555 0142</li>
        <li><svg viewBox="0 0 24 24" aria-hidden="true"><path d="M2 5h20v14H2z M2 5l10 8 10-8" /></svg>kontakt@frischwind-praxis.de</li>
        <li><svg viewBox="0 0 24 24" aria-hidden="true"><circle cx="12" cy="12" r="10"/></svg>www.frischwind-praxis.de</li>
      </ul>
      <p class="contact__address">Lindenallee 12, Musterstadt<br>Nordland, 10115</p>
    </div>
  </section>

  <section class="card card--back" aria-label="Rückseite">
    <div class="brand"><span class="brand__dot"></span>Praxis Frischwind</div>
  </section>
</body>
</html>
```